Business cards, Stationary, E-mail signature, leterhead, fax coversheet, thank you card, invoice tem
Torvan Networks Stationary - please read brief
Business cards, Stationary, E-mail signature, leterhead, fax coversheet, thank you card, invoice tem -
Creative Brief
Use specific fonts
Use the best that will go with the logo design
Professional
Brent Oakley
71523 Birch Ridge Court, Suite 204 Harlow Bend, NV 20783
BrentO@torvannetworks.example
www.torvannetworks.example
Use the icon on the left side of the logo only

```html
<!DOCTYPE html>
<html lang="en">
<head>
<meta charset="utf-8">
<title>Torvan Networks – Business Card</title>
<link rel="stylesheet" href="https://fonts.googleapis.com/css2?family=Roboto:wght@400;500;700&display=swap">
<style>
  :root {
    --stage: #17191c;
    --card-white: #ffffff;
    --brand-navy: #1a3f8f;
    --brand-blue: #2a62c4;
    --brand-cyan: #4fb3e8;
    --swoosh-grey: #c9ccd1;
    --swoosh-light: #e4e6e9;
    --text-dark: #3b3f45;
    --rule: #b8bcc2;
  }
  * { margin: 0; padding: 0; box-sizing: border-box; }
  html, body { width: 1200px; height: 751px; overflow: hidden; }
  body {
    background: var(--stage);
    font-family: "Roboto", Arial, sans-serif;
    position: relative;
  }
  .card {
    position: absolute;
    top: 225px;
    width: 520px;
    height: 300px;
    border-radius: 14px;
    overflow: hidden;
  }
  .card-front { left: 50px; background: var(--card-white); }
  .card-back {
    left: 630px;
    background: radial-gradient(ellipse at 30% 30%, var(--brand-cyan) 0%, var(--brand-blue) 45%, var(--brand-navy) 100%);
  }
  .card-art { position: absolute; inset: 0; width: 100%; height: 100%; }
  .holder-name {
    position: absolute; right: 34px; top: 30px;
    color: #fff; font-weight: 700; font-size: 17px;
  }
  .brand {
    position: absolute; left: 38px; top: 128px;
    display: flex; align-items: center; gap: 12px;
  }
  .brand-dot {
    width: 34px; height: 34px; border-radius: 50%;
    background: var(--brand-navy);
  }
  .brand-name {
    font-weight: 700; font-size: 30px; color: var(--brand-navy);
  }
  .address, .contact {
    position: absolute; top: 208px;
    font-size: 10px; line-height: 14px; color: var(--text-dark);
    font-style: normal;
  }
  .address { left: 38px; }
  .contact { left: 232px; padding-left: 18px; border-left: 1px solid var(--rule); }
  .website {
    position: absolute; left: 250px; top: 268px;
    font-size: 10px; font-weight: 500; color: var(--brand-blue);
  }
  .back-brand {
    position: absolute; right: 30px; bottom: 58px;
    display: flex; align-items: center; gap: 10px;
  }
  .back-brand .brand-dot { background: #fff; width: 26px; height: 26px; }
  .back-brand .brand-name { color: #fff; font-size: 24px; }
</style>
</head>
<body>
  <section class="card card-front" aria-label="Business card front">
    <svg class="card-art" viewBox="0 0 520 300" aria-hidden="true">
      <path d="M0 0 H520 V70 C380 30 200 22 0 48 Z" fill="var(--brand-cyan)"/>
      <path d="M120 0 H520 V108 C450 70 340 40 210 44 C170 45 140 48 110 52 C200 30 250 10 120 0 Z" fill="var(--brand-blue)"/>
      <path d="M0 62 C160 38 340 42 520 120" fill="none" stroke="var(--swoosh-grey)" stroke-width="10"/>
      <path d="M0 76 C170 52 350 58 520 136" fill="none" stroke="var(--swoosh-light)" stroke-width="5"/>
    </svg>
    <div class="holder-name">Brent Oakley</div>
    <div class="brand">
      <span class="brand-dot"></span>
      <span class="brand-name">Torvan Networks</span>
    </div>
    <address class="address">
      71523 Birch Ridge Court<br>Suite 204<br>Harlow Bend, NV 20783
    </address>
    <div class="contact">
      Phone: 555 010 4821<br>Fax: 555 010 4822<br>Email: BrentO@torvannetworks.example
    </div>
    <div class="website">www.torvannetworks.example</div>
  </section>

  <section class="card card-back" aria-label="Business card back">
    <div class="back-brand">
      <span class="brand-dot"></span>
      <span class="brand-name">Torvan Networks</span>
    </div>
  </section>
</body>
</html>
```